BRIXLEY ELECTRICAL

all black background with silver and lime writing, fonts i like are gothic style but am open to ideas, will need a picture logo aswell as im putting this on my van.i am a electrical contractor starting up my own electrical business. underneath brixley electrical heading on card we could put" professiona cost effective soloutions to all your electrical needs".{ or something of that nature }.on aback of card on top half list servises provided, real estate and commercial maintenance, new home and renovation rewires and upgrades, split system air conditioning, floor heat, tv phone data, smoke detoctors, lighting systems , builders welcome, , and also a thankyou for your business.

Industry/Entity Type

Real Estate

Contact Information for Business Card

GAVIN PRESTWORTH
brixleyelectrical@quillnet.com.au
0417352940
lic no 81926
ac lic no l593721
abn 37216405813

```html
<!DOCTYPE html>
<html lang="en">
<head>
<meta charset="utf-8">
<title>Brixley Electrical – Business Card</title>
<link href="https://fonts.googleapis.com/css2?family=PT+Sans+Narrow:wght@400;700&family=Open+Sans:wght@400;600;700&display=swap" rel="stylesheet">
<style>
  :root {
    --stage: #6e4423;
    --card: #0b0b0b;
    --lime: #8cc63f;
    --silver: #d9d9d9;
    --rule: #bdbdbd;
  }
  * { box-sizing: border-box; margin: 0; padding: 0; }
  html, body { width: 1200px; height: 450px; overflow: hidden; }
  body { background: var(--stage); position: relative; font-family: "PT Sans Narrow", "Arial Narrow", sans-serif; }

  .card { position: absolute; top: 58px; width: 555px; height: 342px; background: var(--card); }
  .card--front { left: 35px; }
  .card--back { left: 616px; }

  .brand-name { font-family: "PT Sans Narrow", sans-serif; font-weight: 700; color: var(--lime); letter-spacing: 2px; line-height: 1; }
  .brand-mark { display: inline-block; background: var(--lime); }

  .front-brand { position: absolute; left: 20px; top: 142px; width: 240px; text-align: center; }
  .front-brand .brand-mark { width: 16px; height: 16px; margin-bottom: 10px; }
  .front-brand .brand-name { font-size: 34px; }
  .tagline { position: absolute; left: 10px; top: 240px; width: 260px; text-align: center; color: var(--lime); font-weight: 700; font-size: 19px; line-height: 21px; }

  .contact-frame { position: absolute; left: 270px; top: 0; }
  .contact-name { position: absolute; left: 298px; top: 70px; font-family: "Open Sans", sans-serif; font-weight: 700; font-size: 19px; color: var(--lime); letter-spacing: .3px; }
  .contact-email { position: absolute; left: 298px; top: 130px; font-family: "Open Sans", sans-serif; font-size: 15.5px; color: var(--silver); }
  .contact-phone { position: absolute; left: 300px; top: 158px; font-family: "Open Sans", sans-serif; font-weight: 600; font-size: 18px; color: var(--silver); letter-spacing: 1.5px; }
  .licences { position: absolute; left: 298px; top: 225px; font-family: "Open Sans", sans-serif; font-size: 15.5px; line-height: 21px; color: var(--silver); list-style: none; }

  .services-title { position: absolute; left: 27px; top: 62px; font-weight: 700; font-size: 19px; color: var(--silver); }
  .services { position: absolute; left: 34px; top: 85px; list-style: none; }
  .services li { font-size: 19px; line-height: 25px; color: var(--lime); display: flex; align-items: center; }
  .services .tick { width: 14px; height: 14px; margin-right: 2px; }

  .back-brand { position: absolute; left: 310px; top: 172px; width: 225px; text-align: center; }
  .back-brand .brand-mark { width: 11px; height: 11px; margin-bottom: 7px; }
  .back-brand .brand-name { font-size: 24px; }
  .welcome { position: absolute; left: 300px; top: 246px; width: 245px; text-align: center; color: var(--silver); font-weight: 700; font-size: 19px; }
  .thanks { position: absolute; left: 300px; top: 270px; width: 245px; text-align: center; color: var(--lime); font-weight: 700; font-style: italic; font-size: 19px; }
</style>
</head>
<body>
  <section class="card card--front">
    <div class="front-brand">
      <span class="brand-mark"></span>
      <div class="brand-name">BRIXLEY ELECTRICAL</div>
    </div>
    <p class="tagline">Reliable &amp; Cost Effective Service<br>To All Your Electrical Needs</p>

    <svg class="contact-frame" width="285" height="342" viewBox="0 0 285 342" aria-hidden="true">
      <path d="M72 1 Q12 1 12 60 L12 282 Q12 341 72 341" fill="none" stroke="var(--rule)" stroke-width="3"/>
    </svg>
    <h1 class="contact-name">GAVIN PRESTWORTH</h1>
    <p class="contact-email">brixleyelectrical@quillnet.com.au</p>
    <p class="contact-phone">0417352940</p>
    <ul class="licences">
      <li>Lic. No. 81926</li>
      <li>AC Lic No. l593721</li>
      <li>abn 37216405813</li>
    </ul>
  </section>

  <section class="card card--back">
    <h2 class="services-title">Your one stop shop for all your electrical needs</h2>
    <ul class="services">
      <li><svg class="tick" viewBox="0 0 14 14"><path d="M1 7 L5 12 L13 1" fill="none" stroke="var(--silver)" stroke-width="2"/></svg>Real estate and commercial maintenance</li>
      <li><svg class="tick" viewBox="0 0 14 14"><path d="M1 7 L5 12 L13 1" fill="none" stroke="var(--silver)" stroke-width="2"/></svg>New home and renovation</li>
      <li><svg class="tick" viewBox="0 0 14 14"><path d="M1 7 L5 12 L13 1" fill="none" stroke="var(--silver)" stroke-width="2"/></svg>Rewires and upgrades</li>
      <li><svg class="tick" viewBox="0 0 14 14"><path d="M1 7 L5 12 L13 1" fill="none" stroke="var(--silver)" stroke-width="2"/></svg>Split system air conditioning</li>
      <li><svg class="tick" viewBox="0 0 14 14"><path d="M1 7 L5 12 L13 1" fill="none" stroke="var(--silver)" stroke-width="2"/></svg>Floor heat</li>
      <li><svg class="tick" viewBox="0 0 14 14"><path d="M1 7 L5 12 L13 1" fill="none" stroke="var(--silver)" stroke-width="2"/></svg>TV phone data,</li>
      <li><svg class="tick" viewBox="0 0 14 14"><path d="M1 7 L5 12 L13 1" fill="none" stroke="var(--silver)" stroke-width="2"/></svg>Smoke detectors</li>
      <li><svg class="tick" viewBox="0 0 14 14"><path d="M1 7 L5 12 L13 1" fill="none" stroke="var(--silver)" stroke-width="2"/></svg>Lighting systems</li>
    </ul>
    <div class="back-brand">
      <span class="brand-mark"></span>
      <div class="brand-name">BRIXLEY ELECTRICAL</div>
    </div>
    <p class="welcome">We Welcome Builders</p>
    <p class="thanks">THANK YOU FOR YOUR BUSINESS</p>
  </section>
</body>
</html>
```